Веб-сайт для застройщика под греческую золотую визу Veltaroon.gr
застройщик под греческую золотую визу Veltaroon.gr
Veltaroon.gr
https://morvilo-estates.com/
https://tpk.example/
Veltaroon Development IKE — Website Design Brief
Домен: veltaroon.gr
Название Veltaroon является авторским сочетанием слов:
Hellenic
Premium
Название должно ассоциироваться с:
premium Mediterranean lifestyle
boutique investment real estate
комфортом и эстетикой
Это можно опционально и ненавязчиво обыгрывать в дизайне:
через typography
через premium визуальные акценты
через Mediterranean aesthetic
через сочетание natural + premium visual language
Важно:
Бренд не должен выглядеть overly luxury или “gold-plated wealth style”.
Основной акцент:
tasteful premium
calm confidence
boutique sophistication
1. О компании
Veltaroon Development IKE — девелоперская компания в Греции, которая занимается:
покупкой и реновацией зданий
созданием boutique apartments
продажей недвижимости под Greek Golden Visa
дальнейшим управлением арендой для инвесторов
2. Основная идея сайта
Главный акцент:
Greek Golden Visa
инвестиции в недвижимость в Греции
получение ВНЖ в Европе
комфортный Mediterranean lifestyle
Важно показать, что компания делает проекты «с душой»:
натуральные материалы
светлое дерево
мягкий olive green
уютные современные интерьеры
boutique Mediterranean aesthetics
3. Сайт должен выглядеть
premium
trustworthy
modern
investment-oriented
4. Сайт НЕ должен выглядеть
как агентство недвижимости
как дешёвый Golden Visa landing page
как обычная строительная компания
5. Целевая аудитория
Средний возраст клиентов: 45+ лет, семейные инвесторы, часто ищущие решение для всей семьи.
Инвесторы и семьи из:
Китай
Турция
СНГ
Middle East
Основная цель клиентов:
получение ВНЖ в Европе через Greek Golden Visa
покупка доходной недвижимости
инвестиции в недвижимость в ЕС
6. Основное меню
Greek Golden Visa или просто Golden Visa
Projects
Investors
Partners
Contact (внутри Contact раздела будет вставка About Us либо же вставка будет сразу на главной странице - на ваше усмотрение)
Дополнительно:
Client Login (отдельный кабинет для покупателей квартир / инвесторов)
7. Языки сайта
EN (по умолчанию)
GR
RU
中文
TR
8. Визуальная стилистика
Эстетика
Mediterranean vibe
boutique living vibe
premium natural materials
Цвета:
olive green
warm white
beige
soft stone grey
(Цвета даны справочно и могут адаптироваться дизайнером)
UI стиль:
clean
calm
ВАЖНО:
Полное техническое задание не влезло в описание и размещено в открытом виде на внешнем файлообменнике в текстовом файле:
https://filebarrow.example/k4Rq8
или
https://sklad-faylov.example/7pLmz

```html
<!DOCTYPE html>
<html lang="en">
<head>
<meta charset="utf-8">
<title>Veltaroon — Premium Greek Living &amp; Golden Visa Investments</title>
<link href="https://fonts.googleapis.com/css2?family=Gloock&family=Inter:wght@300;400;500&family=Playfair+Display:ital@1&display=swap" rel="stylesheet">
<style>
:root{
  --warm-white:#f8f6f2;
  --beige:#e7dfd3;
  --card:#f4f1ec;
  --olive:#878154;
  --ink:#2a211c;
  --muted:#6f6760;
  --line:#d9d2c7;
  --brown-dark:#2b1a14;
  --brown-card:#4a342a;
  --cream:#efe6da;
}
*{box-sizing:border-box;margin:0;padding:0}
html,body{width:1200px;height:3495px;overflow:hidden}
body{background:var(--warm-white);color:var(--ink);font-family:"Inter",sans-serif;font-weight:300;position:relative}
.serif{font-family:"Gloock",serif;font-weight:400}
.abs{position:absolute}
.eyebrow{font-size:7px;letter-spacing:.22em;text-transform:uppercase;color:var(--muted);display:flex;align-items:center;gap:8px}
.eyebrow::before,.eyebrow::after{content:"";width:12px;height:1px;background:currentColor;opacity:.6}
.btn{display:inline-flex;align-items:center;gap:10px;font-size:7px;letter-spacing:.2em;text-transform:uppercase;border:1px solid var(--line);padding:0 14px;height:26px;color:var(--ink)}
.body-s{font-size:9px;line-height:1.65;color:#4c443e}

/* header */
.header{top:0;left:0;width:1200px;height:103px;border-bottom:1px solid var(--line)}
.langs{left:149px;top:27px;font-size:9px;color:#aaa;display:flex;gap:9px}
.langs b{color:var(--ink);font-weight:500}
.logo{left:542px;top:22px;display:flex;align-items:center;gap:7px}
.logo-box{width:18px;height:22px;border:1px solid var(--muted)}
.logo-name{font-family:"Gloock",serif;font-size:12px;line-height:1;color:var(--ink)}
.logo-name small{display:block;font-family:"Inter",sans-serif;font-size:6px;letter-spacing:.05em;color:var(--muted)}
.login{left:930px;top:19px;height:28px;border-color:#9a928a}
.nav-rule{left:149px;right:149px;top:67px;height:1px;background:var(--line)}
.nav{left:149px;top:79px;display:flex;gap:43px;font-size:9px;font-weight:400}
.nav .on{color:var(--olive)}
.socials{left:966px;top:73px;display:flex;gap:6px}
.socials span{width:22px;height:22px;border-radius:50%;background:#ece7e0}

/* hero */
.hero{top:103px;left:0;width:1200px;height:475px;background:linear-gradient(100deg,#b19b84 0%,#8d8376 30%,#8aa2b2 55%,#b4c0c4 75%,#c7b7a0 100%)}
.hero-title{left:149px;top:100px;font-size:104px;color:#fff;line-height:1}
.hero-sub{left:150px;top:218px;font-size:30px;color:#fff;line-height:1.15}
.hero-sub i{font-family:"Playfair Display",serif}
.hero .btn-solid{left:149px;top:329px;background:var(--olive);border-color:var(--olive);color:#fff;height:36px}
.hero .btn-ghost{left:312px;top:329px;color:#ddd;border-color:rgba(255,255,255,.6);height:36px}
.arrow-box{width:37px;height:37px;border:1px solid rgba(255,255,255,.6);display:flex;align-items:center;justify-content:center}
.play{left:1124px;top:382px;width:50px;height:50px;border-radius:50%;background:var(--olive);opacity:.9;display:flex;align-items:center;justify-content:center}
.dots{display:flex;gap:7px;align-items:center}
.dots span{width:4px;height:4px;border-radius:50%;background:#fff}
.dots span.on{width:12px;height:12px;background:none;border:1px solid #fff}

/* about */
.about-title{left:149px;top:648px;font-size:40px}
.about-title em{font-style:normal;color:var(--olive)}
.about-lead{left:149px;top:718px;width:310px;font-size:16px;line-height:1.1}
.about-text{left:149px;top:783px;width:300px}
.more{font-size:7px;letter-spacing:.2em;text-transform:uppercase}
.photo-main{left:608px;top:651px;width:432px;height:538px;border-radius:4px;background:linear-gradient(180deg,#d7a27a 0%,#c58a66 45%,#9c6f5b 75%,#e0d3ca 100%)}
.photo-tag{left:618px;top:1162px;background:#fff;font-size:7px;padding:3px 8px}
.photo-small{left:147px;top:1027px;width:154px;height:150px;background:linear-gradient(135deg,#d7b38d,#8a6448 60%,#c08c5c)}
.features{left:149px;top:1246px;width:891px;height:111px;border:1px solid var(--line);display:flex}
.feature{flex:1;display:flex;align-items:center;gap:26px;padding-left:25px;border-right:1px solid var(--line);font-size:9px;line-height:1.5}
.feature:last-child{border-right:0}
.f-icon{width:62px;height:62px;background:#eee9e2;display:flex;align-items:center;justify-content:center}

/* services */
.services{top:1438px;left:0;width:1200px;height:625px;background:var(--beige)}
.center-title{left:0;width:1200px;text-align:center;font-size:40px}
.center-eye{left:0;width:1200px;justify-content:center}
.svc-card{top:185px;width:447px;height:341px;background:var(--warm-white);padding:55px 57px}
.svc-card .bar{width:36px;height:1px;background:var(--muted);margin-bottom:12px}
.svc-card h3{font-size:22px;line-height:1.5;font-weight:400;margin-bottom:22px}
.svc-card p{margin-bottom:18px}

/* portfolio */
.port-card{left:149px;top:2249px;width:901px;height:367px;background:var(--card)}
.port-img{left:155px;top:2255px;width:441px;height:293px;background:linear-gradient(170deg,#a9b2b0 0%,#6d8a86 35%,#4d6a5a 60%,#b58d6b 100%)}
.port-tag{font-size:7px;background:#fff;padding:3px 6px}
.thumb{top:2554px;width:57px;height:56px}
.port-title{left:659px;top:2318px;font-size:24px}
.port-text{left:659px;top:2358px;width:330px;font-size:8.5px}
.spec{top:2496px;width:82px;height:22px;border:1px solid var(--line);font-size:6.5px;display:flex;align-items:center;justify-content:center}
.port-btn{left:659px;top:2531px;width:336px;height:35px;background:var(--olive);color:#fff;justify-content:center;border:0}
.side-card{top:2249px;height:367px;background:var(--card);overflow:hidden}

/* investment */
.invest{top:2766px;left:0;width:1200px;height:729px;background:linear-gradient(180deg,#241611 0%,#2f1d16 60%,#3b271e 100%);color:var(--cream)}
.invest .eyebrow{color:#b9aa9a}
.inv-card{top:306px;width:295px;height:261px;background:var(--brown-card);padding:55px 56px}
.inv-card .bar{width:36px;height:1px;background:#8a7565;margin-bottom:8px}
.inv-card h3{font-size:23px;font-weight:400;margin-bottom:22px}
.inv-card p{font-size:8.5px;line-height:1.65;color:#d8cbbd;margin-bottom:12px}
.inv-card .btn{color:var(--cream);border-color:#9b8576}
</style>
</head>
<body>

<header class="abs header">
  <div class="abs langs"><b>EN</b><span>GR</span><span>RU</span><span>中文</span><span>TR</span></div>
  <div class="abs logo"><span class="logo-box"></span><span class="logo-name">VELTAROON<small>DEVELOPMENT IKE</small></span></div>
  <a class="abs btn login">Client login <span>↗</span></a>
  <div class="abs nav-rule"></div>
  <nav class="abs nav"><span>Greek Golden Visa</span><span>Company</span><span class="on">Projects</span><span>Investors</span><span>Partners</span><span>Golden Visa News</span><span>Golden Visa News</span></nav>
  <div class="abs socials"><span></span><span></span><span></span></div>
</header>

<section class="abs hero" role="img" aria-label="Whitewashed Greek terrace with sofa and potted flowers overlooking a coastal bay">
  <h1 class="abs serif hero-title">Veltaroon</h1>
  <p class="abs serif hero-sub">Premium Greek Living <i>&amp; Golden Visa<br>Investments</i></p>
  <a class="abs btn btn-solid">Explore projects ↗</a>
  <a class="abs btn btn-ghost">Greek golden visa ↗</a>
  <div class="abs arrow-box" style="left:25px;top:219px"><svg width="12" height="6"><path d="M12 3H1M4 0L1 3l3 3" stroke="#fff" fill="none"/></svg></div>
  <div class="abs arrow-box" style="left:1138px;top:219px"><svg width="12" height="6"><path d="M0 3h11M8 0l3 3-3 3" stroke="#fff" fill="none"/></svg></div>
  <div class="abs play"><svg width="10" height="10"><path d="M2 1l7 4-7 4z" stroke="#fff" fill="none"/></svg></div>
  <div class="abs dots" style="left:568px;top:443px"><span></span><span class="on"></span><span></span><span></span><span></span></div>
</section>

<section class="about">
  <div class="abs eyebrow" style="left:149px;top:634px">Welcome to Veltaroon</div>
  <h2 class="abs serif about-title">About <em>Veltaroon</em></h2>
  <p class="abs serif about-lead">Boutique residences thoughtfully designed for modern living and long-term investment</p>
  <p class="abs body-s about-text">Veltaroon Development IKE is a development company in Greece. We are able to breathe new life into ancient buildings, turning them into modern, stylish boutique apartments, where every detail breathes elegance and comfort.</p>
  <span class="abs more" style="left:149px;top:905px">More info &nbsp;↗</span>
  <div class="abs photo-small" role="img" aria-label="Terrace lounge with wicker sofa at sunset over hills"></div>
  <div class="abs photo-main" role="img" aria-label="Woman in a long dress on a seaside balcony at sunset"></div>
  <span class="abs photo-tag">Santorini, Greece</span>
  <div class="abs features">
    <div class="feature"><span class="f-icon"><svg width="26" height="26" fill="none" stroke="#555"><circle cx="13" cy="11" r="8"/><path d="M13 7l1.3 2.6 2.7.4-2 2 .5 2.8-2.5-1.3-2.5 1.3.5-2.8-2-2 2.7-.4z"/><path d="M8 18l-2 6 7-3 7 3-2-6"/></svg></span><span>Premium Greek Golden<br>Visa Company</span></div>
    <div class="feature"><span class="f-icon"><svg width="26" height="26" fill="none" stroke="#555"><rect x="3" y="8" width="20" height="14" rx="2"/><path d="M9 8V5h8v3M3 14h20"/><rect x="11" y="12" width="4" height="4"/></svg></span><span>Comfortable investment property<br>in Greece</span></div>
    <div class="feature"><span class="f-icon"><svg width="26" height="26" fill="none" stroke="#555"><path d="M7 4h12v9H7zM5 13h16v4H5zM7 17v6M19 17v6M3 9v8M23 9v8"/></svg></span><span>Boutique Mediterranean<br>aesthetics</span></div>
  </div>
</section>

<section class="abs services">
  <div class="abs eyebrow center-eye" style="top:78px">Welcome to Veltaroon</div>
  <h2 class="abs serif center-title" style="top:96px">Veltaroon services</h2>
  <article class="abs svc-card" style="left:149px"><div class="bar"></div><h3 class="serif">Investments in projects – raising capital for development</h3><p class="body-s">We understand that investments are not only profitable, but also responsible. That is why we offer an exclusive opportunity to obtain a Greek Golden Visa through the purchase of real estate from Veltaroon Development IKE. This is your chance not only to invest in a promising market, but also to open the door to the limitless possibilities of Europe by obtaining the prestigious status of a resident.</p><a class="btn">Client login ↗</a></article>
  <article class="abs svc-card" style="left:603px"><div class="bar"></div><h3 class="serif">Apartments for sale with<br>guaranteed yield</h3><p class="body-s">We understand that investments are not only profitable, but also responsible. That is why we offer an exclusive opportunity to obtain a Greek Golden Visa through the purchase of real estate from Veltaroon Development IKE. This is your chance not only to invest in a promising market, but also to open the door to the limitless possibilities of Europe by obtaining the prestigious status of a resident.</p><a class="btn">Client login ↗</a></article>
</section>

<section class="portfolio">
  <div class="abs eyebrow center-eye" style="top:2142px">Welcome to Veltaroon</div>
  <h2 class="abs serif center-title" style="top:2160px">Veltaroon portfolio</h2>
  <div class="abs side-card" style="left:0;width:111px"><span class="abs serif" style="left:4px;top:70px;font-size:24px">m²</span><span class="abs" style="left:0;top:293px;width:55px;height:35px;background:var(--olive)"></span></div>
  <div class="abs side-card" style="left:1092px;width:108px"><div class="abs" role="img" aria-label="Coastal bay view" style="left:6px;top:6px;width:102px;height:293px;background:linear-gradient(170deg,#a9b2b0,#4d6a5a)"></div><span class="abs port-tag" style="left:11px;top:14px">Santorini, Greece</span></div>
  <div class="abs port-card"></div>
  <div class="abs port-img" role="img" aria-label="Aerial view of a cliffside village with villas above the sea"></div>
  <span class="abs port-tag" style="left:163px;top:2263px">Santorini, Greece</span>
  <div class="abs thumb" role="img" aria-label="Pool view" style="left:155px;background:#7fa0a8"></div>
  <div class="abs thumb" role="img" aria-label="Garden" style="left:217px;background:#a8a07d"></div>
  <div class="abs thumb" role="img" aria-label="Flowered facade" style="left:278px;background:#b36a6a"></div>
  <div class="abs thumb" role="img" aria-label="Terrace" style="left:340px;background:#8ea4a8"></div>
  <div class="abs thumb" role="img" aria-label="Courtyard flowers" style="left:401px;background:#b27572"></div>
  <div class="abs thumb" role="img" aria-label="Pool" style="left:463px;background:#7b9da4"></div>
  <div class="abs arrow-box" style="left:524px;top:2563px;border-color:var(--line)"><svg width="12" height="6"><path d="M0 3h11M8 0l3 3-3 3" stroke="#999" fill="none"/></svg></div>
  <div class="abs" style="left:659px;top:2305px;width:36px;height:1px;background:var(--muted)"></div>
  <h3 class="abs serif port-title" style="font-weight:400">Villa in Lasithi, Greece, 200 m²</h3>
  <div class="abs body-s port-text"><p>We understand that investments are not only profitable, but also responsible. That is why we offer an exclusive opportunity to obtain a Greek Golden Visa through the purchase of real estate from Veltaroon Development IKE. possibilities of Europe by obtaining the prestigious</p><p style="margin-top:12px">We understand that investments are not only profitable, but also responsible. That is why we offer an exclusive opportunity to obtain a Greek Golden Visa through ...</p></div>
  <span class="abs spec" style="left:659px">⌂ 77 m²</span>
  <span class="abs spec" style="left:743px">▯ 6 rooms</span>
  <span class="abs spec" style="left:827px">☼ 4 beds</span>
  <span class="abs spec" style="left:911px">⌒ 2 bathrooms</span>
  <a class="abs btn port-btn">More info ↗</a>
  <div class="abs dots" style="left:568px;top:2654px"><span style="background:#aaa"></span><span class="on" style="border-color:#aaa"></span><span style="background:#aaa"></span><span style="background:#aaa"></span><span style="background:#aaa"></span></div>
</section>

<section class="abs invest">
  <div class="abs eyebrow" style="left:153px;top:81px">Welcome to Veltaroon</div>
  <h2 class="abs serif" style="left:153px;top:96px;font-size:40px">Investment opportunities</h2>
  <p class="abs serif" style="left:153px;top:166px;width:450px;font-size:16px;line-height:1.1">Boutique residences thoughtfully designed for modern living and long-term investment</p>
  <p class="abs" style="left:153px;top:216px;width:450px;font-size:8.5px;line-height:1.65;color:#d8cbbd">Veltaroon Development IKE is a development company in Greece. We are able to breathe new life into ancient buildings, turning them into modern, stylish boutique apartments, where every detail breathes elegance and comfort.</p>
  <article class="abs inv-card" style="left:153px"><div class="bar"></div><h3 class="serif">Project 1</h3><p>We understand that investments are not only profitable, but also responsible.</p><a class="btn">More info ↗</a></article>
  <article class="abs inv-card" style="left:455px"><div class="bar"></div><h3 class="serif">Project 2</h3><p>We understand that investments are not only profitable, but also responsible.</p><a class="btn">More info ↗</a></article>
  <article class="abs inv-card" style="left:757px"><div class="bar"></div><h3 class="serif">Project 3</h3><p>We understand that investments are not only profitable, but also responsible.</p><a class="btn">More info ↗</a></article>
</section>

</body>
</html>
```